Redesign of iOS App Moriva Tutor

Redesign of existing App Moriva Tutor, an app that helps learning Japanese Kanjis, Hiragana, Katakana.

The functionallity should remain the same as today: the app is free, you may download it at the app store. But: I like the design of my other apps better ;)

Target Market(s)

Students learning Japanese

Industry/Entity Type

Teacher

Font styles to use
Sans Serif

Requirements
Must have
• Moriva Tutor has 7 main screens, all screens has to be designed for iPhone and iPad: Main, Settings, Reading Tests, Writing Tests, Game, Paper Mode, Search
Nice to have
• I like the logo as it is today

```html
<!DOCTYPE html>
<html lang="en">
<head>
<meta charset="utf-8">
<title>Moriva Tutor – Character List</title>
<link href="https://fonts.googleapis.com/css2?family=Montserrat:wght@400;500;600&family=Noto+Sans+JP:wght@400;500&display=swap" rel="stylesheet">
<style>
  :root {
    --ink: #333333;
    --muted: #c4c4c4;
    --accent: #d05a6a;
    --help-red: #c8202f;
    --row-alt: #efefef;
    --row: #ffffff;
    --divider: #c8c8c8;
    --progress-on: #2ecc71;
    --progress-off: #cccccc;
    --star-on: #f5a623;
    --star-off: #cfcfcf;
  }
  * { margin: 0; padding: 0; box-sizing: border-box; }
  html, body { width: 675px; height: 1200px; overflow: hidden; background: var(--row); }
  body { font-family: "Montserrat", sans-serif; color: var(--ink); position: relative; }

  .status-bar { position: absolute; top: 0; left: 0; width: 675px; height: 40px; font-size: 19px; font-family: "Montserrat", sans-serif; font-weight: 500; color: #000; }
  .status-bar .carrier { position: absolute; left: 23px; top: 13px; display: flex; align-items: center; gap: 6px; }
  .status-bar .clock { position: absolute; left: 0; right: 0; top: 13px; text-align: center; font-weight: 600; }
  .status-bar .battery { position: absolute; right: 22px; top: 16px; }

  .search-bar { position: absolute; top: 64px; left: 24px; width: 627px; height: 68px; border-bottom: 1.5px solid var(--divider); }
  .search-bar .search-icon { position: absolute; left: 24px; top: 12px; }
  .search-bar .placeholder { position: absolute; left: 69px; top: 14px; font-size: 21px; color: var(--muted); font-weight: 500; }
  .search-bar .help { position: absolute; right: 27px; top: 14px; display: flex; align-items: center; gap: 6px; color: var(--help-red); font-size: 21px; font-weight: 500; letter-spacing: 0.5px; }

  .char-list { position: absolute; top: 165px; left: 0; width: 675px; list-style: none; }
  .char-row { position: relative; height: 153px; background: var(--row); }
  .char-row:nth-child(odd) { background: var(--row-alt); }

  .glyph { position: absolute; left: 46px; top: 24px; font-family: "Noto Sans JP", sans-serif; font-size: 56px; line-height: 1; color: var(--ink); }
  .glyph.latin { font-family: "Montserrat", sans-serif; font-weight: 500; font-size: 54px; top: 30px; letter-spacing: -1px; }
  .romaji { position: absolute; left: 113px; top: 62px; font-size: 25px; font-weight: 600; color: var(--accent); }
  .progress { position: absolute; left: 46px; top: 102px; display: flex; gap: 9px; }
  .progress span { width: 12px; height: 12px; border-radius: 50%; background: var(--progress-off); }
  .progress span.done { background: var(--progress-on); }
  .script { position: absolute; left: 231px; top: 58px; font-size: 28px; font-weight: 600; color: var(--ink); }
  .level { position: absolute; left: 481px; top: 58px; font-size: 28px; font-weight: 600; color: var(--accent); }
  .favourite { position: absolute; left: 574px; top: 50px; }
</style>
</head>
<body>
  <svg width="0" height="0" style="position:absolute">
    <defs>
      <path id="star-shape" d="M26 2 L32.6 18.8 L50.5 19.7 L36.6 31.1 L41.2 48.5 L26 38.6 L10.8 48.5 L15.4 31.1 L1.5 19.7 L19.4 18.8 Z"/>
    </defs>
  </svg>

  <header class="status-bar">
    <div class="carrier">Carrier
      <svg width="20" height="14" viewBox="0 0 20 14"><path d="M1 5a13 13 0 0 1 18 0" fill="none" stroke="#000" stroke-width="2.2" stroke-linecap="round"/><path d="M4.5 8.3a8 8 0 0 1 11 0" fill="none" stroke="#000" stroke-width="2.2" stroke-linecap="round"/><circle cx="10" cy="12" r="1.9" fill="#000"/></svg>
    </div>
    <div class="clock">1:23 PM</div>
    <svg class="battery" width="44" height="16" viewBox="0 0 44 16"><rect x="0.5" y="0.5" width="39" height="15" rx="3" fill="none" stroke="#000"/><rect x="2.5" y="2.5" width="35" height="11" rx="1.5" fill="#000"/><rect x="41" y="5" width="2.5" height="6" rx="1" fill="#000"/></svg>
  </header>

  <div class="search-bar">
    <svg class="search-icon" width="34" height="36" viewBox="0 0 34 36"><circle cx="14" cy="14" r="11.5" fill="none" stroke="var(--muted)" stroke-width="3"/><line x1="22.5" y1="23" x2="31" y2="32" stroke="var(--muted)" stroke-width="3.2" stroke-linecap="round"/></svg>
    <span class="placeholder">Search...</span>
    <span class="help">
      <svg width="27" height="27" viewBox="0 0 27 27"><circle cx="13.5" cy="13.5" r="12" fill="none" stroke="var(--accent)" stroke-width="2"/><circle cx="14.5" cy="7.6" r="1.6" fill="var(--accent)"/><path d="M13 11.5 L11.6 19.5" stroke="var(--accent)" stroke-width="2.2" stroke-linecap="round"/></svg>
      HELP
    </span>
  </div>

  <ul class="char-list">
    <li class="char-row"><span class="glyph">あ</span><span class="romaji">a</span><div class="progress"><span class="done"></span><span></span><span></span></div><span class="script">Hiragana</span><span class="level">K</span><svg class="favourite" width="54" height="52" viewBox="0 0 52 52"><use href="#star-shape" fill="none" stroke="var(--star-off)" stroke-width="2.5" stroke-linejoin="round"/></svg></li>
    <li class="char-row"><span class="glyph">い</span><span class="romaji">i</span><div class="progress"><span class="done"></span><span></span><span></span></div><span class="script">Hiragana</span><span class="level">K</span><svg class="favourite" width="54" height="52" viewBox="0 0 52 52"><use href="#star-shape" fill="var(--star-on)" stroke="var(--star-on)" stroke-width="2.5" stroke-linejoin="round"/></svg></li>
    <li class="char-row"><span class="glyph">う</span><span class="romaji">u</span><div class="progress"><span class="done"></span><span></span><span></span></div><span class="script">Hiragana</span><span class="level">K</span><svg class="favourite" width="54" height="52" viewBox="0 0 52 52"><use href="#star-shape" fill="none" stroke="var(--star-off)" stroke-width="2.5" stroke-linejoin="round"/></svg></li>
    <li class="char-row"><span class="glyph">え</span><span class="romaji">e</span><div class="progress"><span class="done"></span><span></span><span></span></div><span class="script">Hiragana</span><span class="level">K</span><svg class="favourite" width="54" height="52" viewBox="0 0 52 52"><use href="#star-shape" fill="none" stroke="var(--star-off)" stroke-width="2.5" stroke-linejoin="round"/></svg></li>
    <li class="char-row"><span class="glyph">お</span><span class="romaji">o</span><div class="progress"><span class="done"></span><span></span><span></span></div><span class="script">Hiragana</span><span class="level">K</span><svg class="favourite" width="54" height="52" viewBox="0 0 52 52"><use href="#star-shape" fill="none" stroke="var(--star-off)" stroke-width="2.5" stroke-linejoin="round"/></svg></li>
    <li class="char-row"><span class="glyph">ぐ</span><span class="romaji">gu</span><div class="progress"><span class="done"></span><span></span><span></span></div><span class="script">Hiragana</span><span class="level">K</span><svg class="favourite" width="54" height="52" viewBox="0 0 52 52"><use href="#star-shape" fill="var(--star-on)" stroke="var(--star-on)" stroke-width="2.5" stroke-linejoin="round"/></svg></li>
    <li class="char-row"><span class="glyph latin">gu</span><span class="romaji">a</span><div class="progress"><span class="done"></span><span></span><span></span></div><span class="script">Hiragana</span><span class="level">K</span><svg class="favourite" width="54" height="52" viewBox="0 0 52 52"><use href="#star-shape" fill="none" stroke="var(--star-off)" stroke-width="2.5" stroke-linejoin="round"/></svg></li>
  </ul>
</body>
</html>
```